Bastion Guard Services

Our Company is a security business which needs a cut edge design, the final product should have all relevant information and maintain a bold but modern and professional look.

Target Market(s)

A cut edge design which will attract any audience

Industry/Entity Type

Security

Contact Information for Business Card

BASTION GUARD SERVICES

Daniel Kowalski
Operations Manager
Phone: 0419 357 216

Email: info@bastionguardex.com.au
Web: www.bastionguardex.com.au

Requirements
Must have
• Must be double sided and contain all relevant information and the company logo.

```html
<!DOCTYPE html>
<html lang="en">
<head>
<meta charset="utf-8">
<title>Bastion Guard Services – Business Card</title>
<link href="https://fonts.googleapis.com/css2?family=Arimo:wght@400;700&display=swap" rel="stylesheet">
<style>
  :root {
    --bg: #e4e4e2;
    --card: #ffffff;
    --card-shade: #f1f1f1;
    --slate: #2f4a55;
    --ink: #1c1c1c;
    --accent: #f29a12;
    --divider: #3a3a3a;
  }
  * { margin: 0; padding: 0; box-sizing: border-box; }
  html, body {
    width: 1200px; height: 951px; overflow: hidden;
    background: var(--bg);
    font-family: "Arimo", Arial, sans-serif;
  }
  .canvas {
    position: relative; width: 1200px; height: 951px;
    display: flex; flex-direction: column; align-items: center; justify-content: center; gap: 34px;
  }
  .card {
    position: relative; width: 740px; height: 423px;
    border-radius: 26px;
    background: linear-gradient(135deg, var(--card) 55%, var(--card-shade));
    box-shadow: 0 10px 26px rgba(0,0,0,.18);
    overflow: hidden;
  }
  .brand { display: flex; align-items: center; gap: 14px; }
  .brand-square { width: 34px; height: 34px; background: var(--accent); }
  .brand-name {
    font-weight: 700; color: var(--slate);
    font-size: 38px; letter-spacing: 1px; white-space: nowrap;
  }
  .card-front .brand { position: absolute; left: 70px; top: 186px; }
  .card-back .brand { position: absolute; left: 36px; top: 192px; }
  .card-back .brand-name { font-size: 27px; }
  .card-back .brand-square { width: 26px; height: 26px; }
  .divider {
    position: absolute; left: 338px; top: 60px; width: 3px; height: 300px;
    background: linear-gradient(to bottom, transparent, var(--divider) 30%, var(--divider) 70%, transparent);
  }
  .contact {
    position: absolute; right: 40px; top: 118px; text-align: right;
    color: var(--ink); font-size: 21px; line-height: 1.3;
  }
  .contact-name { font-size: 29px; }
  .contact-role { color: var(--accent); font-size: 19px; margin-bottom: 34px; }
  .accent { color: var(--accent); }
</style>
</head>
<body>
<main class="canvas">
  <section class="card card-front" aria-label="Card front">
    <div class="brand">
      <span class="brand-square"></span>
      <span class="brand-name">BASTION GUARD</span>
    </div>
  </section>

  <section class="card card-back" aria-label="Card back">
    <div class="brand">
      <span class="brand-square"></span>
      <span class="brand-name">BASTION GUARD</span>
    </div>
    <div class="divider"></div>
    <div class="contact">
      <p class="contact-name">Daniel Kowalski</p>
      <p class="contact-role">Operations Manager</p>
      <p>0419 357 216</p>
      <p>info@bastionguardex.com.au</p>
      <p>www.<span class="accent">bastionguardex</span>.com.au</p>
    </div>
  </section>
</main>
</body>
</html>
```